price list for web and print- sending to inquiring clients and use as promo material

Hello
I need a graphic design for my photography price list/s. I am a people photographer. The first of 6 price sheets will be for head shots- I would like a price sheet that captures the prospective clients' attention. The info and visual should be compelling and easy to digest. It should be simple yet interesting. I will provide you with some pictures but you do not have to include them. I have a studio indoors and outdoors also working on location. This design should be for email and print. The picture of "denise" is me and I use that on all my profiles. I like the fonts in the logo but it is too boxy and rigid

Target Market(s)

repeat client, word of mouth referrals, new people but aquaintances of others that might know me

Industry/Entity Type

Graphic Design

Font styles to use
Serif
Sans Serif
Script

Requirements
Must have
• prices and maybe some words about my services that I sent in... Please tie it together as best as possible..
Nice to have
• Loosen up my logo.. it is in a box.....contemporary design but not something that would not fit in with corporate.. I like this headline
• "Create a great first impression with your professional headshots"
• I sent in other copy and my logo(sent in the picture drop box)

```html
<!DOCTYPE html>
<html lang="en">
<head>
<meta charset="utf-8">
<title>Denise M Rowan Photography – Headshot Price List</title>
<link href="https://fonts.googleapis.com/css2?family=Lato:wght@400;700&family=Oswald:wght@400&family=Cormorant+Garamond:ital,wght@1,600&display=swap" rel="stylesheet">
<style>
  :root{
    --backdrop:#1b1b1b;
    --white:#ffffff;
    --ink:#141414;
    --umber:#2f1a19;
    --maroon:#6e1c1f;
    --crimson:#a8282c;
    --crimson-deep:#8c2226;
    --wine:#5a1c1e;
    --wine-deep:#4a1a1b;
    --footer:#3b1f1e;
    --gold:#a8712f;
    --peach:#f3c98d;
    --tan:#b8793c;
    --rose:#f3aaa2;
    --blush:#f7d4cf;
    --photo-a:#9aa0a8;
    --photo-b:#5e646c;
  }
  *{margin:0;padding:0;box-sizing:border-box}
  html,body{width:771px;height:1200px;overflow:hidden;background:var(--backdrop)}
  .sheet{position:absolute;left:100px;top:105px;width:571px;height:988px;background:var(--umber);font-family:"Lato",sans-serif;box-shadow:0 6px 18px rgba(0,0,0,.6)}
  .masthead{position:absolute;left:0;top:0;width:571px;height:153px;background:var(--white)}
  .brand{position:absolute;left:40px;top:30px;width:210px;text-align:center;color:var(--ink)}
  .brand-dba{font-family:"Oswald",sans-serif;font-size:16px;letter-spacing:.3px}
  .brand-name{font-family:"Oswald",sans-serif;font-size:30px;line-height:1.1;margin-top:4px}
  .brand-trade{font-family:"Oswald",sans-serif;font-size:18px;letter-spacing:3px;margin-top:10px}
  .headline{position:absolute;left:298px;top:22px;width:260px;font-family:"Cormorant Garamond",serif;font-style:italic;font-weight:600;font-size:26px;line-height:25px;color:var(--ink)}
  .collage{position:absolute;left:0;top:153px;width:287px;height:360px}
  .features{position:absolute;left:298px;top:160px;width:265px}
  .feature-title{font-size:18px;color:var(--peach);margin-bottom:4px}
  .feature-text{font-size:14px;line-height:18px;color:var(--tan);margin-bottom:12px}
  .band{position:absolute;left:0;top:513px;width:571px;height:47px;background:var(--white);text-align:center;font-size:31px;line-height:47px;color:var(--ink)}
  .band strong{font-weight:700}
  .pkg{position:absolute;padding:14px 0 0 23px;font-size:14px;line-height:18px;color:var(--rose)}
  .pkg-title{text-decoration:underline;text-underline-offset:2px;color:var(--blush)}
  .pkg-entry{left:0;top:560px;width:287px;height:163px;background:var(--crimson);padding-top:20px}
  .pkg-two{left:287px;top:560px;width:284px;height:163px;background:var(--crimson-deep);padding-left:11px;padding-top:12px}
  .pkg-premier{left:0;top:723px;width:287px;height:209px;background:var(--wine);padding-top:14px}
  .pkg-location{left:287px;top:723px;width:284px;height:209px;background:var(--wine-deep);padding-left:11px;padding-top:13px}
  .loc-title{font-size:16px;letter-spacing:4.6px;color:var(--blush);border-bottom:1px solid var(--blush);display:inline-block;padding-bottom:1px;margin-bottom:5px}
  .contact{position:absolute;left:0;top:932px;width:571px;height:56px;background:var(--footer);text-align:center;color:var(--white);font-size:13px;line-height:17px;padding-top:11px}
</style>
</head>
<body>
<main class="sheet">
  <header class="masthead">
    <div class="brand">
      <div class="brand-dba">DMR PHOTO INC dba</div>
      <div class="brand-name">Denise M Rowan</div>
      <div class="brand-trade">PHOTOGRAPHY</div>
    </div>
    <h1 class="headline">Create a great<br>first impression<br>with your<br>professional headshots</h1>
  </header>

  <svg class="collage" width="287" height="360" viewBox="0 0 287 360">
    <defs>
      <linearGradient id="portrait" x1="0" y1="0" x2="1" y2="1">
        <stop offset="0" stop-color="var(--photo-a)"/>
        <stop offset="1" stop-color="var(--photo-b)"/>
      </linearGradient>
    </defs>
    <rect width="287" height="360" fill="var(--umber)"/>
    <polygon points="0,0 40,0 0,40" fill="var(--maroon)"/>
    <polygon points="150,0 287,0 287,20 220,88" fill="var(--gold)"/>
    <polygon points="287,20 287,160 217,90" fill="var(--maroon)"/>
    <polygon points="0,150 0,300 75,225" fill="var(--maroon)"/>
    <polygon points="150,200 220,130 287,197 220,265" fill="#3d2423"/>
    <polygon points="0,330 30,360 0,360" fill="var(--maroon)"/>
    <polygon points="100,360 150,310 200,360" fill="var(--maroon)"/>
    <polygon points="30,0 150,0 95,60 70,40" fill="url(#portrait)" role="img" aria-label="Headshot portrait of a smiling man in a suit"/>
    <polygon points="145,30 225,110 145,190 65,110" fill="url(#portrait)" role="img" aria-label="Headshot portrait of the photographer in a red jacket"/>
    <polygon points="75,140 140,205 75,270 10,205" fill="url(#portrait)" role="img" aria-label="Headshot portrait of a smiling woman in a patterned top"/>
    <polygon points="145,215 220,290 150,360 75,290" fill="url(#portrait)" role="img" aria-label="Headshot portrait of a woman in a dark blazer"/>
    <polygon points="250,230 287,267 287,360 210,360 200,290" fill="url(#portrait)" role="img" aria-label="Headshot portrait of a man in a suit and tie"/>
  </svg>

  <section class="features">
    <h2 class="feature-title">Experience</h2>
    <p class="feature-text">Denise is an accomplished professional photographer who has helped thousands of clients. She is an expert at helping you look confident and approchable</p>
    <h2 class="feature-title">24 Hour Turnaround</h2>
    <p class="feature-text">Your time is valuable. Denise can complete the photoshoot<br>in just 30 minutes.<br>(Or as long as you want.) Our process is designed to save your time.</p>
    <h2 class="feature-title">Enjoyable</h2>
    <p class="feature-text">You can look forward to an enjoyable photo session with Denise’s professional guidance. Denise helps make the experience fun.</p>
  </section>

  <h2 class="band"><strong>Popular</strong> packages</h2>

  <section class="pkg pkg-entry">
    <div class="pkg-title">ENTRY PACKAGE</div>
    Quick and Simple<br>- one pose<br>- one wardrobe<br>- one selected image retouched<br>- just $175<br>- Additional images just $75 each
  </section>

  <section class="pkg pkg-two">
    <div class="pkg-title">2 POSE PACKAGE</div>
    Most Popular<br>- two poses<br>- Two wardrobe changes<br>- Two selected images retouched<br>- One or two background changes<br>- just $175<br>- Additional images just $75 each
  </section>

  <section class="pkg pkg-premier">
    <div class="pkg-title">PREMIER PACKAGE</div>
    Get it all | Most Popular<br>- four poses<br>- 3-4 wardrobe changes<br>- 4 selected images retouched<br>- 2-3 background changes<br>- Additional images just $75 each<br>- optional outdoor studio<br>-Just $525<br>Additional images just $75 each
  </section>

  <section class="pkg pkg-location">
    <div class="loc-title">At your location</div><br>
    $250 set up charge, minimum of 5 people one selected image retouched each additional image $50 each<br>If possible, we like ½ hour appts for each person so they can view their images on the computer<br>5-10 people $150 EACH<br>11-20 people $100 each<br>20+ $75 each
  </section>

  <footer class="contact">
    1840 Laurel Ridge Parkway • Atlanta GA 30318 • 404-555-0172 cell 404-555-0198<br>
    dmrphoto@example.com • http://dmrphoto.com
  </footer>
</main>
</body>
</html>
```